TRU PEAK POWER.

I'd like my business logo.
contact name: Desmond Halvik
phone:0438275160
email: info@trupeakpower.net.au
website: www.trupeakpower.net.au

services:
solar
battery storage
LED lighting
energy saving solutions
general electrical
I'd like the design to look professional

Target Market(s)

Everyone

Industry/Entity Type

Business

Contact Information for Business Card

as described above

Requirements
Must have
• Id like the colours and the design to work well with my logo.

```html
<!DOCTYPE html>
<html lang="en">
<head>
<meta charset="utf-8">
<title>Tru Peak Power – Business Card</title>
<link href="https://fonts.googleapis.com/css2?family=Lato:wght@400;700;900&display=swap" rel="stylesheet">
<style>
  :root {
    --backdrop: #b9bfc6;
    --card: #ffffff;
    --ink: #4a4a4a;
    --rule: #8a8a8a;
    --green: #3fae6a;
    --green-light: #8cc63f;
    --orange: #f5a623;
  }
  * { margin: 0; padding: 0; box-sizing: border-box; }
  html, body { width: 1200px; height: 1000px; overflow: hidden; }
  body {
    background: var(--backdrop);
    font-family: 'Lato', sans-serif;
    position: relative;
  }
  .business-card {
    position: absolute;
    left: 100px; top: 215px;
    width: 1000px; height: 570px;
    background: var(--card);
    box-shadow: 0 12px 30px rgba(0,0,0,0.18);
  }
  .contact-block {
    position: absolute;
    left: 70px; top: 60px;
    width: 470px;
  }
  .contact-name {
    font-size: 44px;
    font-weight: 700;
    color: var(--ink);
    padding-bottom: 10px;
    border-bottom: 2px solid var(--rule);
  }
  .contact-list { list-style: none; padding: 18px 0 20px 30px; border-bottom: 2px solid var(--rule); }
  .contact-item {
    display: flex; align-items: center; gap: 18px;
    font-size: 27px; color: var(--ink);
    height: 58px;
  }
  .contact-icon { width: 30px; height: 30px; flex: none; }
  .brand-lockup {
    position: absolute;
    left: 70px; top: 390px;
    display: flex; align-items: center; gap: 18px;
  }
  .brand-dot { width: 60px; height: 60px; border-radius: 50%; background: var(--orange); }
  .brand-name {
    font-size: 48px; font-weight: 900; color: var(--green);
    letter-spacing: 1px;
  }
  .services {
    position: absolute;
    left: 60px; right: 40px; top: 505px;
    font-size: 23px; font-weight: 700; color: var(--green);
    letter-spacing: 1px; white-space: nowrap;
  }
  .services .sep { color: var(--orange); font-weight: 400; margin: 0 6px; }
  .brand-artwork {
    position: absolute;
    right: 30px; top: 40px;
    width: 380px; height: 380px;
    border-radius: 50%;
    background: radial-gradient(circle at 60% 55%, var(--green-light) 0%, var(--green) 38%, rgba(245,166,35,0.85) 40%, rgba(245,166,35,0.25) 70%, rgba(255,255,255,0) 72%);
  }
</style>
</head>
<body>
  <main class="business-card">
    <section class="contact-block">
      <h1 class="contact-name">Desmond Halvik</h1>
      <ul class="contact-list">
        <li class="contact-item">
          <svg class="contact-icon" viewBox="0 0 30 30" aria-hidden="true"><rect x="2" y="7" width="26" height="17" fill="var(--green)"/><path d="M2 7 L15 17 L28 7" fill="none" stroke="#fff" stroke-width="2"/></svg>
          <span>info@trupeakpower.net.au</span>
        </li>
        <li class="contact-item">
          <svg class="contact-icon" viewBox="0 0 30 30" aria-hidden="true"><rect x="8" y="2" width="14" height="26" rx="3" fill="none" stroke="var(--green)" stroke-width="2.5"/><circle cx="15" cy="24" r="1.5" fill="var(--green)"/></svg>
          <span>0438 275 160</span>
        </li>
        <li class="contact-item">
          <svg class="contact-icon" viewBox="0 0 30 30" aria-hidden="true"><circle cx="15" cy="15" r="12" fill="none" stroke="var(--green)" stroke-width="2.5"/><ellipse cx="15" cy="15" rx="5" ry="12" fill="none" stroke="var(--green)" stroke-width="2"/><line x1="3" y1="15" x2="27" y2="15" stroke="var(--green)" stroke-width="2"/></svg>
          <span>www.trupeakpower.net.au</span>
        </li>
      </ul>
    </section>

    <div class="brand-lockup">
      <span class="brand-dot"></span>
      <span class="brand-name">TRU PEAK POWER</span>
    </div>

    <p class="services">SOLAR<span class="sep">|</span>BATTERY STORAGE<span class="sep">|</span>LED LIGHTING<span class="sep">|</span>ENERGY SAVING SOLUTIONS</p>

    <div class="brand-artwork" role="img" aria-label="Large brand emblem area: orange sun rays around a green leaf light bulb"></div>
  </main>
</body>
</html>
```